rose gold typography style landscape business card | upmarket tanning lounge

After years of receiving spray tans, we are two young professionals starting our own spray tanning business. Our point of difference is offering a complete tanning experience within a fun, edgy yet professional atmosphere.
Our ideal card would draw upon design elements from the typography example we have attached. We are hoping to have "velmira" in all lowercase in the typography style, with "TANNING LOUNGE" in much smaller uppercase font underneath but closely positioned below "velmira".
We have attached an example of a business card created by a designer on here - we like how the word on the front almost goes beyond the edges of the card itself.
But you have the design know how, so please let your creative juices flow!
We are thinking either rose gold text (matte rather than a chrome look) with a white background or rose gold freehand style typography with a charcoal background using landscape orientation. We have opted for a thicker style edgy typography to accommodate the metallic look font we are looking for.
We cannot wait to see what you create! Thanks in advance.
Harriet & Jocelyn
Project Deadline Extended
Reason: Firstly, we wish to thank each and every one of you who have provided a submission for our project. You guys are amazingly talented and we've loved watching all the designs come through.
We have decided to take our top four favourite designs to a poll with our friends and family and will therefore need to extend the deadline by a couple of days.
We do apologise for any inconvenience this may have caused and thank you for your patience and understanding!
Harriet & Jocelyn

```html
<!DOCTYPE html>
<html lang="en">
<head>
<meta charset="utf-8">
<title>velmira tanning lounge – business card</title>
<link rel="stylesheet" href="https://fonts.googleapis.com/css2?family=Dancing+Script:wght@500&family=Open+Sans:wght@300&display=swap">
<style>
  :root {
    --page-bg: #ffffff;
    --card-charcoal: #58595b;
    --rose-gold: #c4876a;
    --rose-gold-soft: #c9a08f;
    --contact-white: #f4f1ef;
  }
  html, body {
    margin: 0;
    padding: 0;
    width: 1200px;
    height: 911px;
    overflow: hidden;
    background: var(--page-bg);
  }
  .canvas {
    position: relative;
    width: 1200px;
    height: 911px;
  }
  .business-card {
    position: absolute;
    left: 150px;
    top: 205px;
    width: 900px;
    height: 500px;
    background: var(--card-charcoal);
    overflow: hidden;
  }
  .brand-name {
    position: absolute;
    left: 92px;
    top: 60px;
    margin: 0;
    font-family: "Dancing Script", cursive;
    font-weight: 500;
    font-size: 200px;
    line-height: 1;
    color: var(--rose-gold);
    letter-spacing: 2px;
  }
  .brand-tagline {
    position: absolute;
    left: 100px;
    top: 292px;
    margin: 0;
    font-family: "Open Sans", sans-serif;
    font-weight: 300;
    font-size: 24px;
    letter-spacing: 1px;
    color: var(--rose-gold-soft);
  }
  .contact {
    position: absolute;
    left: 520px;
    top: 300px;
    color: var(--contact-white);
  }
  .contact-names {
    margin: 0 0 8px;
    font-family: "Dancing Script", cursive;
    font-weight: 500;
    font-size: 27px;
    letter-spacing: 1px;
  }
  .contact-phone {
    display: flex;
    align-items: center;
    gap: 10px;
    margin: 0;
    font-family: "Dancing Script", cursive;
    font-weight: 500;
    font-size: 25px;
    letter-spacing: 4px;
  }
  .phone-icon {
    width: 22px;
    height: 16px;
    fill: var(--contact-white);
  }
</style>
</head>
<body>
  <main class="canvas">
    <section class="business-card" aria-label="velmira tanning lounge business card">
      <h1 class="brand-name">velmira</h1>
      <p class="brand-tagline">TANNING LOUNGE</p>
      <div class="contact">
        <p class="contact-names">Harriet &amp; Jocelyn</p>
        <p class="contact-phone">
          <svg class="phone-icon" viewBox="0 0 22 16" aria-hidden="true">
            <path d="M1 5 Q11 -1 21 5 L19 8 L15 6.5 L15 4.5 Q11 3.5 7 4.5 L7 6.5 L3 8 Z"/>
            <path d="M6 8 L16 8 L19 15 L3 15 Z"/>
          </svg>
          <span>0047385291</span>
        </p>
      </div>
    </section>
  </main>
</body>
</html>
```